POP/ROCK artist: CD Cover Design Project

IF U LOVE MUSIC AND ALBUM COVER ART THEN PLEASE PARTICIPATE IN MY PROJECT AND HAVE A GREAT TIME DESIGNING SOMETHING UNIQUE AND EXCITING!!!!
Hi, my name is tovo, a pop/rock artist living in Europe. i just finished recording a fun dance song, called SPINNIN WILD HEARTS, with a successful Brightfield Records producer in Europe and I just put the finishing touches on the music video shot in LA. Now i'm going to release the song and video with PulsaWave. It's going to go out to about 750 stores, including SongCrate, tunebox and all the other biggies as well as a load of smaller ones.
I need a great looking CD cover design that i can plaster everywhere . . . and i really mean everywhere i can.
As per PulsaWave' specs, the cover art MUST BE 1500 x 1500 pixels. It cannot be blurry or pixilated and must be perfectly square.
I've uploaded some pics for you to choose from but you can use whichever one(s) you like . . . or none of them if you prefer, according to your inspiration. Just let me know if you want other pics and i can upload others.
Updates
Hey there,
Hey there,
Hi again, all,
Hey there,
Hi there, designers!
Hello everybody,
Target Market(s)
Modern pop/rock radio listeners of Kestrel Radio, ZPX, etc.
Please click on the following link to see the music video and hear the song:
http://www.clipvault.example/watch?v=Qr7tLm2Wd9a
Also, i have various pics and photos i can upload . . . just tell me what you need!!!!!
Requirements
Must have
- As per PulsaWave' specs, the cover art MUST BE 1500 x 1500 pixels. It cannot be blurry or pixilated and must be perfectly square.
My artist name, tovo, and the song title, Spinnin Wild Hearts, must be on the cover art.
The destination for your design is online music stores like SongCrate. So the dimensions will be VERY SMALL The actual size seen by the public will be about 1.5 cm x 1.5 cm! (Please have a look at the SongCrate store to see the actual size people will view the designs in.)
This means that your designs have to be clearly communicated at that size. The title of the song (spinnin wild hearts) and my artist name (tovo) have to be large enough to read and whatever idea you're going for has to be easily understood.
Nice to have
- It should look totally modern and pop/rock, hip and cool. It's up to you and your design magic to do whatever you think it takes.
Should not have
- Website and e-mail addresses CANNOT be included anywhere on cover art.

```html
<!DOCTYPE html>
<html lang="en">
<head>
<meta charset="utf-8">
<title>tovo – Spinnin Wild Hearts</title>
<link rel="stylesheet" href="https://fonts.googleapis.com/css2?family=Questrial&family=Merriweather:ital,wght@1,900&display=swap">
<style>
  :root {
    --page-bg: #3a3a3a;
    --gold-edge: #c98a12;
    --gold-mid: #e3a92c;
    --core-amber: #e6ab3a;
    --ring-cyan: #86d9e2;
    --ring-lime: #d9d25a;
    --glow-cream: #f6d27a;
    --ink: #141414;
    --title-glow: rgba(255, 238, 170, 0.85);
    --figure-dark: #1d1d1f;
    --figure-mid: #4a4a46;
  }
  * { margin: 0; padding: 0; box-sizing: border-box; }
  html, body {
    width: 1200px;
    height: 900px;
    overflow: hidden;
    background: var(--page-bg);
  }
  .cover {
    position: absolute;
    left: 222px;
    top: 72px;
    width: 756px;
    height: 756px;
    overflow: hidden;
    background:
      radial-gradient(ellipse 70% 30% at 50% 100%, var(--glow-cream) 0%, rgba(246,210,122,0) 100%),
      radial-gradient(circle at 69% 33%,
        var(--core-amber) 0%,
        var(--core-amber) 8%,
        #b9cf8a 17%,
        var(--ring-cyan) 24%,
        var(--ring-cyan) 30%,
        #b8dba0 38%,
        var(--ring-lime) 44%,
        var(--gold-mid) 58%,
        var(--gold-edge) 85%,
        #b97a0c 100%);
  }
  .cover__artist-photo {
    position: absolute;
    left: 446px;
    top: 78px;
    width: 222px;
    height: 466px;
    border-radius: 46% 46% 8% 8% / 18% 18% 4% 4%;
    background: linear-gradient(180deg, var(--figure-mid) 0%, var(--figure-dark) 45%, var(--figure-dark) 100%);
    opacity: 0.92;
  }
  .cover__artist-name {
    position: absolute;
    left: 213px;
    top: 428px;
    font-family: "Questrial", "Helvetica Neue", sans-serif;
    font-size: 46px;
    letter-spacing: 0.42em;
    color: var(--ink);
    line-height: 1;
  }
  .cover__title {
    position: absolute;
    left: 0;
    width: 100%;
    top: 608px;
    text-align: center;
    font-family: "Merriweather", Georgia, serif;
    font-style: italic;
    font-weight: 900;
    font-size: 62px;
    line-height: 1;
    color: var(--ink);
    text-shadow:
      -3px 3px 0 var(--title-glow),
      -6px 6px 8px rgba(0, 0, 0, 0.45);
  }
</style>
</head>
<body>
  <section class="cover">
    <div class="cover__artist-photo" role="img" aria-label="Photo of the artist standing in a long dark coat, playing an electric guitar"></div>
    <p class="cover__artist-name">tovo</p>
    <h1 class="cover__title">Spinnin Wild Hearts</h1>
  </section>
</body>
</html>
```